Sell the dream! Property investment proposal document

We are looking for a proposal document which outlines our vision for property development. The purpose of the document is to raise investment from investors - sell the dream!
Brief summary:
Tarrow Dwellings Developments, is an emerging New Zealand property investment company with a focus on providing unique property investment opportunities.
Our expertise and capabilities in architectural modular homes provide us with a remarkable advantage in tackling the development of properties that are typically considered challenging, remote, or uniquely positioned.
Our specialization in this niche sector of property development not only sets us apart from competitors, but also paves the way for lucrative investment opportunities in the New Zealand property market.
Feel free to use any images from www.tarrowdwellings.co.nz
Target Market(s)
investors for a unique property development opportunity
Industry/Entity Type
luxury property development in unique locations throughout New Zealand
Font styles to use
Colors
Designer to choose only greyscale colors for use in the design.
Look and feel

```html
<!DOCTYPE html>
<html lang="en">
<head>
<meta charset="utf-8">
<title>Tarrow Dwellings Developments – Investment Proposal</title>
<link href="https://fonts.googleapis.com/css2?family=Inter:wght@400;600;700&display=swap" rel="stylesheet">
<style>
  :root {
    --canvas: #e8e8e9;
    --paper: #ffffff;
    --paper-soft: #f4f4f4;
    --charcoal: #333333;
    --charcoal-deep: #2a2a2a;
    --ink: #1f1f1f;
    --muted: #8a8a8a;
    --text-light: #d9d9d9;
    --white: #ffffff;
  }
  * { box-sizing: border-box; margin: 0; padding: 0; }
  html, body { width: 667px; height: 1200px; overflow: hidden; }
  body { background: var(--canvas); font-family: "Inter", Arial, sans-serif; position: relative; }

  .spread { position: absolute; left: 113px; width: 440px; height: 310px; display: flex; }
  .spread--cover { top: 67px; }
  .spread--story { top: 445px; }
  .spread--value { top: 823px; }
  .page { position: relative; width: 220px; height: 310px; overflow: hidden; }

  /* Cover spread */
  .page--light { background: var(--paper); }
  .cover-panel { position: absolute; left: 13px; top: 13px; width: 194px; height: 240px; }
  .cover-panel--dark { background: var(--charcoal); }
  .contact { position: absolute; left: 0; right: 0; top: 150px; text-align: center; color: var(--text-light); font-size: 3.6px; line-height: 1.6; }
  .contact__name { font-weight: 700; color: var(--white); }
  .contact__gap { height: 5px; }
  .cover-photo { background: linear-gradient(180deg, #f2ddc4 0%, #c9b29b 30%, #6d6a66 55%, #3b3a38 80%, #2a2a29 100%); }
  .cover-title { position: absolute; left: 12px; bottom: 14px; color: var(--white); font-weight: 700; font-size: 13px; line-height: 1.12; letter-spacing: -0.2px; }
  .page-footer { position: absolute; left: 13px; right: 13px; bottom: 16px; display: flex; justify-content: space-between; align-items: center; }
  .wordmark { font-size: 11px; font-weight: 400; color: var(--ink); letter-spacing: 0.2px; }
  .partner { display: flex; align-items: center; gap: 4px; }
  .partner__square { width: 9px; height: 9px; background: var(--ink); }
  .partner__name { font-size: 3.4px; line-height: 1.2; color: var(--ink); width: 26px; }
  .partner__rule { width: 1px; height: 9px; background: var(--ink); margin-left: 2px; }

  /* Story spread */
  .page--dark { background: var(--charcoal); }
  .copy { position: absolute; color: var(--text-light); font-size: 3.7px; line-height: 1.55; }
  .copy h2 { color: var(--white); font-size: 6.2px; font-weight: 700; margin-bottom: 6px; }
  .copy p { margin-bottom: 5px; }
  .copy--overview { left: 13px; top: 20px; width: 76px; }
  .photo-pale { position: absolute; left: 100px; top: 0; width: 120px; height: 160px; background: linear-gradient(180deg, #f6f6f6 0%, #e4e4e4 100%); }
  .photo-dusk { position: absolute; left: 100px; top: 160px; width: 120px; height: 150px; background: linear-gradient(180deg, #8a8e87 0%, #40433d 45%, #5c5a3f 80%, #7d7650 100%); }
  .photo-pale--spill { left: 0; width: 55px; }
  .photo-dusk--spill { left: 0; width: 55px; }
  .photo-interior { position: absolute; left: 62px; top: 13px; width: 145px; height: 110px; background: linear-gradient(180deg, #d8d6d2 0%, #b9b6b0 55%, #8d8984 100%); }
  .copy--origins { left: 62px; top: 138px; width: 145px; }

  /* Value spread */
  .page--soft { background: var(--paper-soft); }
  .copy--dark-ink { color: #444; }
  .copy--dark-ink h2 { color: var(--ink); }
  .copy--advantage { left: 13px; top: 16px; width: 194px; }
  .copy--finance { left: 13px; top: 16px; width: 194px; }
  .photo-coast { position: absolute; left: 0; top: 138px; width: 220px; height: 172px; background: linear-gradient(180deg, #d7dde2 0%, #c4ccd2 35%, #6f7466 60%, #5d7a3d 80%, #7a9a45 100%); }
  .photo-ridge { position: absolute; left: 0; top: 138px; width: 220px; height: 172px; background: linear-gradient(180deg, #9c8d78 0%, #6d6352 35%, #3f3d33 60%, #56542f 82%, #6b6535 100%); }
</style>
</head>
<body>

  <section class="spread spread--cover" aria-label="Back and front cover">
    <div class="page page--light">
      <div class="cover-panel cover-panel--dark">
        <div class="contact">
          <div class="contact__name">Sam Reid</div>
          <div>Chief Executive</div>
          <div class="contact__gap"></div>
          <div>+64 21 555 0148</div>
          <div>sam@tarrowdwellings.co.nz</div>
          <div>www.tarrowdwellings.co.nz</div>
        </div>
      </div>
      <div class="page-footer">
        <span class="wordmark">Tarrow</span>
        <span class="partner"><span class="partner__square"></span><span class="partner__name">Tarrow Dwellings Developments</span><span class="partner__rule"></span></span>
      </div>
    </div>
    <div class="page page--light">
      <div class="cover-panel cover-photo" role="img" aria-label="Modern glass home on a hillside at sunset">
        <div class="cover-title">Delivered and<br>connected<br>anywhere</div>
      </div>
      <div class="page-footer">
        <span class="wordmark">Tarrow</span>
        <span class="partner"><span class="partner__square"></span><span class="partner__name">Tarrow Dwellings Developments</span><span class="partner__rule"></span></span>
      </div>
    </div>
  </section>

  <section class="spread spread--story" aria-label="Business overview and origins">
    <div class="page page--dark">
      <div class="copy copy--overview">
        <h2>Business Overview</h2>
        <p>Tarrow Dwellings Developments is a New Zealand company creating architectural modular homes for remote, challenging and uniquely positioned sites across the country.</p>
        <p>Our homes are built off site to a precise standard, then delivered and connected wherever the land allows, from coastal ridges to alpine valleys.</p>
        <p>This approach shortens build times, reduces site risk and opens up land that traditional builders overlook, creating value for every investor.</p>
        <p>We partner with landowners, councils and trusted trades to bring each project from concept to completion with care.</p>
      </div>
      <div class="photo-pale" role="img" aria-label="Bright minimal exterior wall"></div>
      <div class="photo-dusk" role="img" aria-label="Dark modular home among grassland"></div>
    </div>
    <div class="page page--dark">
      <div class="photo-pale photo-pale--spill" role="img" aria-label="Bright minimal exterior wall, continued"></div>
      <div class="photo-dusk photo-dusk--spill" role="img" aria-label="Dark modular home among grassland, continued"></div>
      <div class="photo-interior" role="img" aria-label="Light living room with ocean view"></div>
      <div class="copy copy--origins">
        <h2>Business Origins</h2>
        <p>The business began with a simple idea: that exceptional places deserve exceptional homes, no matter how difficult the access.</p>
        <p>Early projects proved that modular construction could meet luxury expectations while keeping costs predictable and timelines short.</p>
        <p>Today we combine design, engineering and logistics expertise under one roof, ready to scale across New Zealand.</p>
      </div>
    </div>
  </section>

  <section class="spread spread--value" aria-label="Competitive advantage and financial summary">
    <div class="page page--soft">
      <div class="copy copy--dark-ink copy--advantage">
        <h2>Competitive Advantage</h2>
        <p>Our modular expertise lets us develop sites that others consider too remote or complex, giving investors access to rare land at sensible prices.</p>
        <p>Controlled factory builds mean fewer delays, consistent quality and a faster path to returns.</p>
      </div>
      <div class="photo-coast" role="img" aria-label="Dark modular home on a green coastal hill with rocks"></div>
    </div>
    <div class="page page--dark">
      <div class="copy copy--finance">
        <h2>Financial Summary</h2>
        <p>Each development is modelled on conservative sale values and fixed build costs, giving investors clear visibility of expected returns.</p>
        <p>Capital is staged across land purchase, manufacture and delivery, with regular reporting at every milestone.</p>
        <p>Projected returns reflect strong demand for unique luxury homes in sought-after New Zealand locations.</p>
      </div>
      <div class="photo-ridge" role="img" aria-label="Home on a rural ridge at dusk"></div>
    </div>
  </section>

</body>
</html>
```